Business Cards, Letterhead and Email signature for Halvern Building Collective
Halvern Building Collective
Professional
Doran Pellick
Partner
Office: 4100 Birchmont Ave Suite 900 Charlotte, NC 28211
Mailing: 5217 Birchmont Ave #482 Charlotte, NC 28211
dpellick@halvernbuildingcoll.example
halvvernbuildingcoll.example
I am open to ideas, maybe the logo with a matching background color. Be creative

```html
<!DOCTYPE html>
<html lang="en">
<head>
<meta charset="utf-8">
<title>Halvern Building Collective — Stationery</title>
<link href="https://fonts.googleapis.com/css2?family=Open+Sans:wght@400;600;700&display=swap" rel="stylesheet">
<style>
  :root{
    --navy:#1b3a86;
    --blue:#2a5cb8;
    --sky:#9fb6e0;
    --grey:#8b95a5;
    --ink:#3b4250;
    --paper:#ffffff;
    --ground:#e9ebef;
    --rule:#d9dde5;
  }
  *{box-sizing:border-box;margin:0;padding:0}
  html,body{width:1200px;height:754px;overflow:hidden}
  body{background:var(--ground);font-family:"Open Sans",Arial,sans-serif;color:var(--ink);position:relative}
  .sheet{position:absolute;background:var(--paper);box-shadow:0 2px 8px rgba(20,30,60,.15);overflow:hidden}

  /* plain footer bar */
  .footer-bar{position:absolute;left:0;right:0;bottom:0;height:26px;background:var(--blue);border-top:3px solid var(--sky)}
  .footer-bar--tall{height:34px}

  .brand{display:flex;align-items:center;gap:6px;color:var(--navy);font-weight:700;font-size:10px;line-height:1.1;text-transform:uppercase;letter-spacing:.4px}
  .brand-square{width:12px;height:12px;background:var(--navy);flex:none}
  .brand-name{max-width:110px}
  .brand--light{color:#fff}
  .brand--light .brand-square{background:#fff}
  .tiny{font-size:6px;line-height:1.45;color:var(--grey)}

  /* address slip */
  .slip{left:40px;top:40px;width:360px;height:170px}
  .slip .brand{position:absolute;left:24px;top:22px}
  .slip .tiny{position:absolute;left:24px;top:56px}

  /* name slip */
  .name-slip{left:40px;top:230px;width:360px;height:170px}
  .name-slip .brand{position:absolute;left:24px;top:22px}
  .name-slip .person{position:absolute;right:28px;bottom:50px;text-align:right}
  .person-name{font-size:14px;color:var(--navy);font-weight:600}
  .person-role{font-size:8px;color:var(--grey)}

  /* letterhead */
  .letterhead{left:440px;top:30px;width:300px;height:424px}
  .letterhead .brand{position:absolute;left:24px;top:24px}
  .head-address{position:absolute;right:22px;top:22px;text-align:right}
  .letter-body{position:absolute;left:24px;right:24px;top:78px;font-size:6.3px;line-height:1.6;color:var(--ink)}
  .letter-body p{margin-bottom:6px}
  .signature{width:70px;height:16px;background:linear-gradient(90deg,#c9cfdd,#e5e8ef);margin:6px 0 2px}
  .seal{position:absolute;left:108px;top:300px;width:22px;height:22px;border:1.5px solid #7fa6a8;border-radius:50%}

  /* invoice */
  .invoice{left:790px;top:30px;width:300px;height:424px}
  .invoice .brand{position:absolute;left:24px;top:24px}
  .invoice-title{position:absolute;left:24px;top:76px;font-size:10px;font-weight:700;color:var(--navy);letter-spacing:1px}
  .invoice-meta{position:absolute;right:24px;top:76px;font-size:6px;color:var(--grey);line-height:1.8;text-align:right}
  .invoice-billto{position:absolute;left:24px;top:104px;font-size:6px;color:var(--grey)}
  .invoice-table{position:absolute;left:24px;top:140px;border-collapse:collapse;font-size:6px;width:252px}
  .invoice-table th{background:var(--rule);color:var(--ink);text-align:left;padding:3px 4px;font-weight:600}
  .invoice-table td{height:14px;border-bottom:1px solid #eceef2;padding:0 4px}
  .invoice-table .amount{text-align:right}
  .invoice-table .total td{background:var(--rule);font-weight:600}

  /* business cards */
  .card-back{left:50px;top:450px;width:330px;height:190px;background:var(--blue)}
  .card-back .brand{position:absolute;left:50%;top:50%;transform:translate(-50%,-50%);font-size:13px}
  .card-back .brand-name{max-width:170px}
  .card-back .brand-square{width:16px;height:16px}
  .card-front{left:425px;top:480px;width:330px;height:190px}
  .card-front .brand{position:absolute;left:22px;top:20px}
  .card-front .person{position:absolute;right:22px;top:22px;text-align:right}
  .card-front .contact{position:absolute;left:22px;top:62px}

  /* envelope */
  .envelope{left:790px;top:490px;width:370px;height:190px}
  .envelope .brand{position:absolute;left:22px;top:20px}
  .envelope .tiny{position:absolute;left:22px;top:52px}
</style>
</head>
<body>

<section class="sheet slip">
  <div class="brand"><span class="brand-square"></span><span class="brand-name">Halvern Building Collective</span></div>
  <p class="tiny">4100 Birchmont Ave Suite 900<br>Charlotte, NC 28211<br>halvvernbuildingcoll.example</p>
  <div class="footer-bar"></div>
</section>

<section class="sheet name-slip">
  <div class="brand"><span class="brand-square"></span><span class="brand-name">Halvern Building Collective</span></div>
  <div class="person">
    <p class="person-name">Doran Pellick</p>
    <p class="person-role">Partner</p>
  </div>
  <div class="footer-bar"></div>
</section>

<section class="sheet letterhead">
  <div class="brand"><span class="brand-square"></span><span class="brand-name">Halvern Building Collective</span></div>
  <p class="tiny head-address">4100 Birchmont Ave Suite 900<br>Charlotte, NC 28211<br>halvvernbuildingcoll.example</p>
  <div class="letter-body">
    <p>Dear Client,</p>
    <p>Thank you for considering our team for your upcoming project. We bring careful planning, honest pricing and steady crews to every site we build.</p>
    <p>Our partners oversee each phase from early design through final inspection, keeping owners informed and schedules on track.</p>
    <p>We look forward to working with you and will follow up shortly with a detailed proposal.</p>
    <p>Sincerely,</p>
    <div class="signature" role="img" aria-label="Handwritten signature"></div>
    <p>Doran Pellick, Partner</p>
  </div>
  <span class="seal" aria-hidden="true"></span>
  <div class="footer-bar footer-bar--tall"></div>
</section>

<section class="sheet invoice">
  <div class="brand"><span class="brand-square"></span><span class="brand-name">Halvern Building Collective</span></div>
  <p class="tiny head-address">5217 Birchmont Ave #482<br>Charlotte, NC 28211<br>dpellick@halvernbuildingcoll.example</p>
  <p class="invoice-title">INVOICE</p>
  <p class="invoice-meta">Date: ________<br>Invoice No: ________</p>
  <p class="invoice-billto">Bill To:</p>
  <table class="invoice-table">
    <tr><th>Description</th><th class="amount">Amount</th></tr>
    <tr><td></td><td></td></tr>
    <tr><td></td><td></td></tr>
    <tr><td></td><td></td></tr>
    <tr><td></td><td></td></tr>
    <tr><td></td><td></td></tr>
    <tr class="total"><td>Total</td><td></td></tr>
  </table>
  <div class="footer-bar footer-bar--tall"></div>
</section>

<section class="sheet card-back">
  <div class="brand brand--light"><span class="brand-square"></span><span class="brand-name">Halvern Building Collective</span></div>
</section>

<section class="sheet card-front">
  <div class="brand"><span class="brand-square"></span><span class="brand-name">Halvern Building Collective</span></div>
  <div class="person">
    <p class="person-name">Doran Pellick</p>
    <p class="person-role">Partner</p>
  </div>
  <p class="tiny contact">Office: 4100 Birchmont Ave Suite 900 Charlotte, NC 28211<br>Mailing: 5217 Birchmont Ave #482 Charlotte, NC 28211<br>dpellick@halvernbuildingcoll.example<br>halvvernbuildingcoll.example</p>
  <div class="footer-bar"></div>
</section>

<section class="sheet envelope">
  <div class="brand"><span class="brand-square"></span><span class="brand-name">Halvern Building Collective</span></div>
  <p class="tiny">4100 Birchmont Ave Suite 900<br>Charlotte, NC 28211</p>
</section>

</body>
</html>
```